Bramblewick Gardening Services. A6 flyer single sided

Need an A6 flyer designing. Single sided.
I am a gardener.
I do lawn mowing - one-off garden tidy ups or regular fortnightly visits.
All kinds of trees expertly felled, topped or pruned.
Hedge cutting.
Fencing replaced or repaired.
Fully insured.
Access to fully qualified and licenced tree arborist
07724 316048 or 01632 742918.

I have attached my business card and letter head logo.
I'm open to new designs without incorporating any of my artwork.

Industry/Entity Type

Gardener

```html
<!DOCTYPE html>
<html lang="en">
<head>
<meta charset="utf-8">
<title>Bramblewick Garden Services – Flyer</title>
<link href="https://fonts.googleapis.com/css2?family=Roboto+Condensed:wght@700&family=Roboto:wght@400;500;700&display=swap" rel="stylesheet">
<style>
  :root{
    --green-dark:#0d6b2c;
    --green:#1f8f3a;
    --green-mid:#3aa63c;
    --lime:#a9cf2f;
    --lime-light:#d3e85a;
    --orange:#ee5a24;
    --orange-dark:#d2421a;
    --ink:#1e1e1e;
    --text:#2b2b2b;
    --paper:#ffffff;
    --paper-grey:#ececec;
  }
  *{margin:0;padding:0;box-sizing:border-box}
  html,body{width:946px;height:1200px;overflow:hidden;background:#f2f2f2}
  .flyer{
    position:relative;width:946px;height:1200px;overflow:hidden;
    background:linear-gradient(180deg,var(--paper) 55%,var(--paper-grey) 100%);
    font-family:"Roboto",Arial,sans-serif;color:var(--text);
  }
  .header-art{position:absolute;left:0;top:0;width:946px;height:600px}
  .brand{position:absolute;left:50px;top:48px;color:#fff}
  .brand-name{
    font-family:"Roboto Condensed","Arial Narrow",sans-serif;font-weight:700;
    font-size:78px;line-height:1;letter-spacing:1px;text-transform:uppercase;
    text-shadow:0 2px 4px rgba(0,0,0,.25);
  }
  .brand-tagline{margin-top:16px;font-weight:700;font-size:34px;letter-spacing:.3px}
  .badge{
    position:absolute;left:655px;top:358px;width:210px;height:210px;border-radius:50%;
    background:radial-gradient(circle at 40% 35%,#ff7a3d 0%,var(--orange) 55%,var(--orange-dark) 100%);
    border:8px solid #fff;box-shadow:0 0 0 4px var(--lime),0 4px 10px rgba(0,0,0,.3);
    display:flex;flex-direction:column;align-items:center;justify-content:center;
    color:#fff;font-weight:700;font-size:44px;line-height:1.05;transform:rotate(-8deg);
  }
  .services{position:absolute;left:50px;top:600px;width:540px}
  .services-title{color:var(--green);font-weight:500;font-size:36px;line-height:1.15;margin-bottom:20px}
  .service-list{list-style:none}
  .service-list li{
    position:relative;padding-left:46px;font-size:25px;line-height:1.3;margin-bottom:8px;
  }
  .service-list svg{position:absolute;left:0;top:6px;width:26px;height:22px}
  .contact{position:absolute;left:50px;top:1048px;width:560px;white-space:nowrap}
  .contact-name{color:var(--green);font-weight:700;font-size:30px;line-height:1.15;margin-bottom:8px}
  .contact-phones{color:var(--ink);font-weight:700;font-size:35px;line-height:1.15;letter-spacing:.2px}
  .email-tab{
    position:absolute;left:0;bottom:0;width:450px;height:52px;
    background:var(--orange);border-top-right-radius:40px;
    color:#fff;font-size:25px;font-weight:500;line-height:52px;padding-left:52px;white-space:nowrap;
  }
  .photo{
    position:absolute;left:622px;width:276px;border-radius:16px;
  }
  .photo-hedge-trim{top:592px;height:186px;background:linear-gradient(160deg,#7a8f5c 0%,#3f8a2a 45%,#2f6f1f 100%)}
  .photo-mowing{top:790px;height:192px;background:linear-gradient(200deg,#2b5a1c 0%,#3f8a2a 45%,#c8323a 60%,#6a9a3a 100%)}
  .photo-pressure-wash{top:994px;height:194px;background:linear-gradient(150deg,#a6735a 0%,#b98a6a 40%,#d9d4cc 60%,#8b5e48 100%)}
</style>
</head>
<body>
<main class="flyer">
  <svg class="header-art" viewBox="0 0 946 600" aria-hidden="true">
    <defs>
      <linearGradient id="headerGreen" x1="0" y1="0" x2="0.4" y2="1">
        <stop offset="0" stop-color="#0f6a2d"/>
        <stop offset="0.6" stop-color="#2a9a3c"/>
        <stop offset="1" stop-color="#57b23a"/>
      </linearGradient>
      <linearGradient id="swooshLime" x1="0" y1="1" x2="1" y2="0">
        <stop offset="0" stop-color="#1f8f3a"/>
        <stop offset="0.5" stop-color="#7fbf2f"/>
        <stop offset="1" stop-color="#d3e85a"/>
      </linearGradient>
    </defs>
    <path d="M0 0 H946 V280 C820 420 600 520 360 540 C230 550 110 535 0 510 Z" fill="url(#headerGreen)"/>
    <path d="M0 560 C150 590 330 585 480 560 C700 520 860 400 946 230 V300 C850 450 680 540 470 575 C300 600 140 600 0 590 Z" fill="url(#swooshLime)"/>
    <path d="M946 20 C900 10 860 30 820 0 H946 Z M860 0 C920 60 946 120 946 170 V0 Z" fill="#7fbf2f" opacity=".8"/>
    <path d="M890 0 C946 80 946 160 930 230" stroke="#d3e85a" stroke-width="10" fill="none"/>
    <path d="M0 315 C200 280 420 290 620 300 C760 308 860 330 946 330 V360 C850 470 650 540 420 555 C260 565 120 555 0 535 Z"
          fill="#2e7a22" role="img" aria-label="Photo of a neatly trimmed green hedge"/>
  </svg>

  <header class="brand">
    <h1 class="brand-name">Bramblewick<br>Garden Services</h1>
    <p class="brand-tagline">&amp; Exterior Property Maintenance</p>
  </header>

  <div class="badge"><span>Fully</span><span>Insured</span></div>

  <section class="services">
    <h2 class="services-title">Our Services</h2>
    <ul class="service-list">
      <li><svg viewBox="0 0 28 24"><path d="M2 13 L10 21 L26 3" stroke="var(--green)" stroke-width="4" fill="none"/></svg>Regular fortnightly visits or one-off<br>garden tidy ups</li>
      <li><svg viewBox="0 0 28 24"><path d="M2 13 L10 21 L26 3" stroke="var(--green)" stroke-width="4" fill="none"/></svg>All kinds of trees expertly felled,<br>topped or pruned</li>
      <li><svg viewBox="0 0 28 24"><path d="M2 13 L10 21 L26 3" stroke="var(--green)" stroke-width="4" fill="none"/></svg>Hedge cutting</li>
      <li><svg viewBox="0 0 28 24"><path d="M2 13 L10 21 L26 3" stroke="var(--green)" stroke-width="4" fill="none"/></svg>Lawn mowing, Pruning, Strimming</li>
      <li><svg viewBox="0 0 28 24"><path d="M2 13 L10 21 L26 3" stroke="var(--green)" stroke-width="4" fill="none"/></svg>Fencing replaced or repaired</li>
      <li><svg viewBox="0 0 28 24"><path d="M2 13 L10 21 L26 3" stroke="var(--green)" stroke-width="4" fill="none"/></svg>Access to fully qualified and<br>licenced tree arborist</li>
    </ul>
  </section>

  <div class="photo photo-hedge-trim" role="img" aria-label="Photo of a gardener trimming a hedge with a hedge trimmer"></div>
  <div class="photo photo-mowing" role="img" aria-label="Photo of a red lawn mower cutting grass"></div>
  <div class="photo photo-pressure-wash" role="img" aria-label="Photo of a block paving driveway being pressure washed"></div>

  <section class="contact">
    <p class="contact-name">Call @ ROB HALLIDAY:</p>
    <p class="contact-phones">07724 316048 or 01632 742918</p>
  </section>

  <footer class="email-tab">bramblewick@mailbox.co.uk</footer>
</main>
</body>
</html>
```